Flyer Design

A childminding business - looking after babies from 1 years old to preschool 4 years.
Values are based on parents trusting me to look after their precious young baby through to 3 years old, images should include a male and female cute baby of about 9-18 months old. I operate from a smaller home not nursery environment which is why parents choose to place with me. My business name is Tovalin so branding should have a Tovalin image possibly carrying a baby.
I am providing care and learning through diverse play opportunities inside and outside the home, a focus on learning outdoors with nature is good.
the colors should communicate trust, peace and calm in a safe any happy natural(not classroom)environment.
Can you touch up my facial image to tidy hair, smooth jawline and change colour of jacket to match overall theme.

```html
<!DOCTYPE html>
<html lang="en">
<head>
<meta charset="utf-8">
<title>Tovalin Childminding Services – Flyer</title>
<link href="https://fonts.googleapis.com/css2?family=Bevan&family=Mulish:wght@400;600&family=Noto+Sans:wght@400;600&display=swap" rel="stylesheet">
<style>
  :root {
    --teal: #a8dbd4;
    --teal-deep: #8ccdc4;
    --teal-text: #2f5f66;
    --pink: #ef7fa8;
    --pink-strong: #ec5f96;
    --ink: #444a4f;
    --paper: #ffffff;
    --mist: #ebebeb;
    --backdrop: #e4e2de;
  }
  * { box-sizing: border-box; margin: 0; padding: 0; }
  html, body { width: 825px; height: 1200px; overflow: hidden; background: var(--backdrop); }
  .flyer {
    position: absolute; left: 28px; top: 57px;
    width: 670px; height: 945px;
    transform: scale(1.15); transform-origin: top left;
    background: linear-gradient(180deg, var(--paper) 20%, var(--mist) 60%, var(--paper) 92%);
    font-family: "Noto Sans", sans-serif; color: var(--ink);
    overflow: hidden;
  }
  .flyer__shapes { position: absolute; inset: 0; }
  .brand { position: absolute; left: 32px; top: 18px; }
  .brand__name {
    font-family: "Bevan", serif; font-size: 54px; line-height: 1;
    font-weight: 400; color: var(--pink-strong);
  }
  .brand__tagline {
    font-family: "Mulish", sans-serif; font-size: 27px; line-height: 1.2;
    color: var(--teal-text); margin-top: 4px;
  }
  .logo-mark {
    position: absolute; left: 462px; top: 166px; width: 200px;
    display: flex; align-items: center; justify-content: center; gap: 10px;
    font-family: "Bevan", serif; font-size: 30px; color: var(--pink-strong);
  }
  .logo-mark__dot { width: 16px; height: 16px; border-radius: 50%; background: var(--teal-deep); }
  .services {
    position: absolute; left: 26px; top: 210px; width: 320px;
    list-style: none; font-size: 15.5px; line-height: 19.6px;
  }
  .services li, .approach li { position: relative; padding-left: 16px; }
  .services li::before, .approach li::before {
    content: ""; position: absolute; left: 0; top: 6px;
    width: 7px; height: 7px; border-radius: 50%; background: var(--pink);
  }
  .photo { position: absolute; }
  .photo--baby { left: 12px; top: 332px; width: 380px; height: 220px;
    background: radial-gradient(ellipse at 45% 55%, #f3e6dc 0%, #f4f1ee 55%, #ececec 100%); }
  .photo--play { left: 0; top: 620px; width: 314px; height: 260px;
    background: linear-gradient(160deg, #f4f4f4 0%, #eae6ea 55%, #e7dfe8 100%); }
  .photo--minder { left: 470px; top: 420px; width: 158px; height: 158px; border-radius: 50%;
    background: radial-gradient(circle at 50% 45%, #b49488 0%, #5b4440 60%, #2a2324 100%); }
  .contact {
    position: absolute; left: 0; top: 552px; width: 454px; height: 60px;
    background: var(--pink); border-radius: 0 14px 14px 0;
    padding: 9px 0 0 26px; color: #fff;
    font-family: "Bevan", serif; font-size: 19px; line-height: 1.2;
  }
  .contact__email { font-size: 14.5px; }
  .minder-name {
    position: absolute; left: 424px; top: 617px; width: 200px; text-align: center;
    font-family: "Mulish", sans-serif; font-size: 27px; font-weight: 400; color: var(--ink);
  }
  .approach { position: absolute; left: 319px; top: 659px; width: 330px; }
  .approach__title { width: 300px; font-weight: 600; font-size: 15px; line-height: 19px; margin-bottom: 10px; }
  .approach ul { list-style: none; font-size: 13.5px; line-height: 17px; }
  .approach li { margin-bottom: 8px; padding-left: 21px; }
  .approach li::before { left: 2px; top: 5px; }
  .registration {
    position: absolute; left: 322px; top: 855px;
    font-size: 16.5px; line-height: 1; letter-spacing: 0.5px; color: var(--pink-strong);
  }
  .footer-band {
    position: absolute; left: 0; top: 887px; width: 670px; height: 58px;
    background: var(--teal); display: flex; align-items: center; justify-content: center;
    font-family: "Mulish", sans-serif; font-size: 15.4px; color: var(--ink);
  }
</style>
</head>
<body>
<main class="flyer">
  <svg class="flyer__shapes" width="670" height="945" viewBox="0 0 670 945" aria-hidden="true">
    <path d="M0 0 H560 V270 L400 230 C300 150 150 130 0 158 Z" fill="var(--teal)"/>
    <path d="M0 158 C150 130 300 150 400 230 L420 262 C320 200 150 176 0 200 Z" fill="var(--pink)"/>
    <circle cx="560" cy="190" r="195" fill="var(--pink)"/>
    <circle cx="575" cy="195" r="185" fill="var(--paper)"/>
    <path d="M600 455 L670 448 V502 L600 492 Z" fill="var(--pink)"/>
    <circle cx="549" cy="499" r="92" fill="var(--teal)"/>
  </svg>

  <header class="brand">
    <h1 class="brand__name">Tovalin</h1>
    <p class="brand__tagline">Childminding Services</p>
  </header>

  <div class="logo-mark"><span class="logo-mark__dot"></span>Tovalin</div>

  <ul class="services">
    <li>Registering children from<br>6 months</li>
    <li>Before and after school care working<br>from St Aldric's, North Fenmore<br>and Larkhill schools</li>
    <li>Ad hoc sessions available</li>
  </ul>

  <div class="photo photo--baby" role="img" aria-label="Smiling baby wrapped in a soft white blanket"></div>

  <div class="photo photo--minder" role="img" aria-label="Portrait of the childminder"></div>

  <div class="contact">
    <p>Contact Marla 0700-900-1234</p>
    <p class="contact__email">Email: Tovalinchildminding@maildesk.net</p>
  </div>

  <h2 class="minder-name">Marla Quinby</h2>

  <div class="photo photo--play" role="img" aria-label="Two toddlers cheering while playing with colourful toys"></div>

  <section class="approach">
    <p class="approach__title">Delivering the Early Years Foundation Stage through:</p>
    <ul>
      <li>Building secure attachments to enable learning</li>
      <li>Creative, physical, messy and imaginative play<br>in a comfortable home setting</li>
      <li>A strong focus on building communication and<br>language skills</li>
      <li>A large garden perfect for free movement and<br>discovery</li>
    </ul>
  </section>

  <p class="registration">OFSTED REGISTRATION NO: EY512304</p>

  <footer class="footer-band">Located in W19 close to Hollyvale Lane&nbsp;|&nbsp; Call to arrange a viewing</footer>
</main>
</body>
</html>
```